New letter head for Air Conditioning business

We need a new professional letter head design to suit our new re-branded air conditioning business. Our new logo is attached

```html
<!DOCTYPE html>
<html lang="en">
<head>
<meta charset="utf-8">
<title>Vega Air Conditioning &amp; Refrigeration – Letterhead</title>
<link href="https://fonts.googleapis.com/css2?family=Open+Sans:ital,wght@0,400;0,600;0,700;1,400&display=swap" rel="stylesheet">
<style>
  :root {
    --backdrop: #e6ecec;
    --paper: #ffffff;
    --ink: #3a3a3c;
    --ink-soft: #6b6b6e;
    --brand-green: #63bf86;
    --brand-red: #ef6b5d;
    --brand-dark: #353538;
    --signature-tone: #dcdcde;
  }
  * { box-sizing: border-box; margin: 0; padding: 0; }
  html, body {
    width: 1200px; height: 800px; overflow: hidden;
    background: var(--backdrop);
    font-family: "Open Sans", Arial, sans-serif;
    color: var(--ink);
  }
  .canvas {
    width: 1200px; height: 800px;
    display: flex; align-items: center; justify-content: center;
  }
  .letterhead {
    position: relative;
    width: 540px; height: 764px;
    background: var(--paper);
    box-shadow: 0 6px 24px rgba(0,0,0,.12);
    padding: 46px 52px 40px 52px;
    font-size: 9.6px; line-height: 1.5;
  }
  .brand {
    position: absolute; top: 40px; right: 52px;
    display: flex; align-items: center; gap: 8px;
  }
  .brand-dot {
    width: 22px; height: 22px; border-radius: 50%;
    background: var(--brand-green);
  }
  .brand-name {
    font-size: 20px; font-weight: 600; letter-spacing: 2px;
    color: var(--brand-dark);
  }
  .letter-date { margin-top: 62px; }
  .recipient { margin-top: 10px; line-height: 1.45; font-style: italic; }
  .salutation { margin-top: 26px; font-weight: 700; }
  .letter-body p { margin-top: 14px; text-indent: 14px; }
  .letter-body p:first-child { margin-top: 10px; }
  .closing { margin-top: 34px; }
  .signature {
    display: block; width: 120px; height: 26px; margin: 8px 0 6px 0;
    background: var(--signature-tone); border-radius: 3px;
  }
  .signer-name { font-weight: 700; }
  .signer-company { color: var(--ink-soft); }
  .contact-block {
    position: absolute; left: 52px; bottom: 56px;
    line-height: 1.55; font-style: normal;
  }
  .contact-company { color: var(--brand-green); text-transform: uppercase; }
  .contact-label { color: var(--brand-red); }
</style>
</head>
<body>
<main class="canvas">
  <article class="letterhead">
    <header class="brand">
      <span class="brand-dot" aria-hidden="true"></span>
      <span class="brand-name">VEGA</span>
    </header>

    <p class="letter-date">10 September, 2020</p>
    <address class="recipient">
      Mr. Daniel R. Ashford<br>
      President<br>
      BB Holdings<br>
      2276 Maple Ridge Rd. Easton,<br>
      VA 22300-1100
    </address>

    <p class="salutation">Dear Mr Daniel</p>

    <section class="letter-body">
      <p>Contrary to popular belief, Lorem Ipsum is not simply random text. It has roots in a piece of classical Latin literature from 45 BC, making it over 2000 years old. Henry Waldmere, a Latin professor at Larkfield College in Brenton, looked up one of the more obscure Latin words, consectetur, from a Lorem Ipsum passage, and going through the cites of the word in classical literature, discovered the undoubtable source.</p>
      <p>Lorem Ipsum comes from sections 1.10.32 and 1.10.33 of "de Summis Rebus Humanis" (The Extremes of Good and Evil) by Aurelian Tullo, written in 45 BC. This book is a treatise on the theory of ethics, very popular during the Renaissance. Lorem Ipsum used since the 1500s is reproduced below for those interested. Sections 1.10.32 and 1.10.33 from "de Summis Rebus Humanis" by Aurelian Tullo are also reproduced in</p>
      <p>Contrary to popular belief, Lorem Ipsum is not simply random text. It has roots in a piece of classical Latin literature from 45 BC, making it over 2000 years old. Henry Waldmere, a Latin professor at Larkfield College in Brenton, looked up one of the more obscure Latin words.</p>
    </section>

    <footer class="closing">
      <p>Sincerely your</p>
      <span class="signature" role="img" aria-label="Handwritten signature"></span>
      <p class="signer-name">Peter L. Garrison</p>
      <p class="signer-company">Company name</p>
    </footer>

    <address class="contact-block">
      <p class="contact-company">Vega Air Conditioning &amp; Refrigeration</p>
      <p>4812 Linden Hwy, Oakdale,</p>
      <p><span class="contact-label">Tel:</span>(555)010-2233 <span class="contact-label">Fax:</span>(555)010-4455</p>
      <p><span class="contact-label">Email:</span>hello@vegaaircooling.com</p>
    </address>
  </article>
</main>
</body>
</html>
```